Marine Business Card

We install Lighting, Sound, Video, PA Systems to hotels, nightclubs, Restaurants, Cruise Ships.

Target Market(s)

We want to focus on the Marine or Maritime/Cruise industry. Passenger ships and cruise liners are the companies we want to appeal to

Industry/Entity Type

Business

Contact Information for Business Card

Mark Tilbury
Managing Director
Harbourne Vista Audio Marine Ltd

Requirements
Must have
• Office: 01632 960482
Mobile: 07700 900317
mark@harbournevistaaudio.co.uk
www.harbournevistaaudio.co.uk

```html
<!DOCTYPE html>
<html lang="en">
<head>
<meta charset="utf-8">
<title>Harbourne Vista Audio Marine Ltd – Business Card</title>
<link rel="stylesheet" href="https://fonts.googleapis.com/css2?family=Comfortaa:wght@400;700&display=swap">
<style>
  :root {
    --card-bg: #fff6b8;
    --frame: #2b2b2b;
    --brand-blue: #2c4295;
    --text-grey: #6b7396;
    --outline: #111111;
    --white: #ffffff;
    --eq-blue: #1d8fc4;
    --eq-indigo: #2b2fd6;
    --eq-violet: #6a1f9a;
    --eq-magenta: #c21a66;
    --eq-red: #d8232a;
    --eq-orange: #e2661c;
    --eq-yellow: #f4d21c;
  }
  html, body {
    margin: 0;
    padding: 0;
    width: 1200px;
    height: 776px;
    overflow: hidden;
    background: var(--white);
  }
  .card {
    position: relative;
    box-sizing: border-box;
    width: 1200px;
    height: 776px;
    background: var(--card-bg);
    border: 4px solid var(--frame);
    border-radius: 8px;
    overflow: hidden;
    font-family: "Comfortaa", sans-serif;
  }
  .brand-name {
    position: absolute;
    left: 90px;
    top: 100px;
    margin: 0;
    font-size: 68px;
    font-weight: 700;
    color: var(--brand-blue);
    letter-spacing: 1px;
    line-height: 1;
    white-space: nowrap;
  }
  .company-line {
    position: absolute;
    left: 96px;
    top: 224px;
    margin: 0;
    font-size: 28px;
    font-weight: 700;
    line-height: 1.2;
    color: var(--white);
    -webkit-text-stroke: 4px var(--outline);
    paint-order: stroke fill;
    letter-spacing: 0.3px;
    white-space: nowrap;
  }
  .contact {
    position: absolute;
    right: 44px;
    top: 70px;
    margin: 0;
    text-align: right;
    font-style: normal;
    color: var(--brand-blue);
    font-size: 15px;
    line-height: 1.7;
    white-space: nowrap;
  }
  .contact-name {
    display: block;
    font-size: 22px;
    font-weight: 700;
    line-height: 1.3;
  }
  .contact-role {
    display: block;
    color: var(--text-grey);
    font-weight: 700;
    margin-bottom: 8px;
  }
  .contact-label {
    font-weight: 700;
  }
  .equaliser-band {
    position: absolute;
    left: 0;
    right: 0;
    top: 330px;
    bottom: 0;
    background:
      linear-gradient(to bottom, var(--card-bg) 0%, rgba(255, 246, 184, 0.6) 18%, rgba(255, 246, 184, 0) 30%),
      linear-gradient(to right, var(--eq-blue) 0%, var(--eq-indigo) 30%, var(--eq-violet) 45%,
        var(--eq-magenta) 58%, var(--eq-red) 72%, var(--eq-orange) 86%, var(--eq-yellow) 100%);
  }
</style>
</head>
<body>
  <div class="card">
    <p class="brand-name">Harbourne Vista</p>
    <p class="company-line">Harbourne Vista Audio Marine Ltd</p>
    <address class="contact">
      <span class="contact-name">Mark Tilbury</span>
      <span class="contact-role">Managing Director</span>
      <span class="contact-label">Office:</span> 01632 960482<br>
      <span class="contact-label">Mobile:</span> 07700 900317<br>
      mark@harbournevistaaudio.co.uk<br>
      www.harbournevistaaudio.co.uk
    </address>
    <div class="equaliser-band" role="img" aria-label="Colourful pixel equaliser pattern running from blue through purple and red to yellow"></div>
  </div>
</body>
</html>
```